NZ First of it's kind solutions directory and marketplace for busy Mums needs a business card design

We need a business card design for our new nationwide business in NZ (long term plans to go global). We provide solutions to the everyday challenges that busy Mums face by connecting them with quality communities and suppliers of carefully selected, relevant products and services. We sell direct via our online marketplace. The final design should communicate our values of inclusivity, quality and smart solutions. Colours should incorporate our logo colour palette of #477077 and #6ba8b2. Our website is at https://www.brightnestly.com

Target Market(s)

busy Mums, Age 28 – 50, female, income over $100K, location main centres NZ primarily but NZ wide. Is likely juggling work or career with a young family. Probably had hobbies which have fallen by the wayside.
-Wants to succeed in her chosen career without compromising on family life
-to successfully juggle her career without feeling like she is compromising her children
- Is time poor, something always has to give and it’s generally her health (she’ll stay up late, get stressed)
- probably ex corporate or professional career. Has discretional income

Industry/Entity Type

Business

Contact Information for Business Card

Lena Hartwell, Founder, BrightNestly.com (Strapline Click; Connect; Done), 48 Kowhai Terrace, Ferndale, Auckland 1071, New Zealand. Mob: 021 437 518 Ph: +64 (0)9 581 4706

Font styles to use
Other font styles liked:
• Raleway, and/or Architects Daughter

Colors
00a990
33b8a4
86cfc6
cfeae6

Requirements
Must have
• the above details, streamline. the logo and colours associated with those logos
Should not have
• foil or metallic colours

```html
<!DOCTYPE html>
<html lang="en">
<head>
<meta charset="utf-8">
<title>BrightNestly – Business Card</title>
<link rel="stylesheet" href="https://fonts.googleapis.com/css2?family=Arimo:wght@400;700&display=swap">
<style>
  :root {
    --teal-dark: #477077;
    --teal-light: #6ba8b2;
    --ink: #333a3c;
    --paper: #ffffff;
    --backdrop: #eceeee;
  }
  * { box-sizing: border-box; margin: 0; padding: 0; }
  html, body {
    width: 1200px; height: 900px; overflow: hidden;
    background: var(--backdrop);
    font-family: "Arimo", Arial, sans-serif;
  }
  .canvas {
    position: relative; width: 1200px; height: 900px;
    display: flex; flex-direction: column; align-items: center; justify-content: center; gap: 50px;
  }
  .card {
    position: relative; width: 560px; height: 320px; overflow: hidden;
    box-shadow: 0 6px 18px rgba(0,0,0,.18);
  }
  /* Back of card */
  .card--back { background: var(--teal-dark); display: flex; align-items: center; justify-content: center; }
  .brand { display: flex; align-items: center; gap: 14px; }
  .brand__dot { width: 34px; height: 34px; border-radius: 50%; }
  .brand__name { font-weight: 700; letter-spacing: -0.5px; }
  .card--back .brand__dot { width: 54px; height: 54px; background: var(--paper); }
  .card--back .brand__name { font-size: 46px; color: var(--paper); }
  /* Front of card */
  .card--front { background: var(--paper); }
  .card__wave { position: absolute; inset: 0; }
  .person { position: absolute; left: 40px; top: 40px; }
  .person__name { font-size: 21px; font-weight: 700; letter-spacing: 0.5px; color: var(--teal-dark); }
  .person__surname { color: var(--teal-light); }
  .person__role { font-size: 15px; color: var(--ink); margin-top: 2px; }
  .card--front .brand { position: absolute; right: 28px; top: 48px; gap: 10px; }
  .card--front .brand__dot { background: var(--teal-dark); }
  .card--front .brand__name { font-size: 33px; color: var(--teal-dark); }
  .contact { position: absolute; left: 40px; top: 158px; font-size: 16px; color: var(--ink); line-height: 21px; }
  .contact__line { display: flex; align-items: center; gap: 6px; }
  .contact__icon { width: 14px; height: 14px; fill: var(--ink); }
  .contact__address { margin-top: 12px; }
  .website { position: absolute; right: 26px; top: 226px; font-size: 13px; color: var(--paper); }
</style>
</head>
<body>
<main class="canvas">
  <section class="card card--back" aria-label="Card back">
    <div class="brand">
      <span class="brand__dot"></span>
      <span class="brand__name">BrightNestly</span>
    </div>
  </section>

  <section class="card card--front" aria-label="Card front">
    <svg class="card__wave" viewBox="0 0 560 320" aria-hidden="true">
      <path d="M0,262 C230,312 420,205 560,150 L560,320 L0,320 Z" fill="var(--teal-light)"/>
      <path d="M0,283 C235,322 425,214 560,166 L560,320 L0,320 Z" fill="var(--paper)"/>
      <path d="M0,292 C240,328 430,220 560,172 L560,320 L0,320 Z" fill="var(--teal-dark)"/>
    </svg>

    <div class="person">
      <p class="person__name">LENA <span class="person__surname">HARTWELL</span></p>
      <p class="person__role">Founder</p>
    </div>

    <div class="brand">
      <span class="brand__dot"></span>
      <span class="brand__name">BrightNestly</span>
    </div>

    <div class="contact">
      <p class="contact__line">
        <svg class="contact__icon" viewBox="0 0 16 16"><path d="M2 6c0-2 3-3 6-3s6 1 6 3v1h-3V5.5C10 5 6 5 5 5.5V7H2z M4 8h8l1 5H3z"/></svg>
        021 437 518
      </p>
      <p class="contact__line">
        <svg class="contact__icon" viewBox="0 0 16 16"><path d="M4 1h8v14H4z M5.5 2.5v9h5v-9z" fill-rule="evenodd"/></svg>
        +64 (0)9 581 4706
      </p>
      <p class="contact__address">48 Kowhai Terrace, Ferndale<br>Auckland 1071, New Zealand</p>
    </div>

    <p class="website">www.BrightNestly.com</p>
  </section>
</main>
</body>
</html>
```